TALRENO Business Cards

We require a business card for our company that provides IT consulting services. We already have a logo that needs to be used on the card. We want a clean professional looking design that incorporates our colours. Our main focus is providing managed services to business, which involves us looking after all of their IT requirements including managing servers/networks, projects, and procurement.

Industry/Entity Type

Information Technology

Requirements
Must have
• our logo, contact information, name, title, phone numbers

```html
<!DOCTYPE html>
<html lang="en">
<head>
<meta charset="utf-8">
<title>TALRENO Business Cards</title>
<link href="https://fonts.googleapis.com/css2?family=Arimo:wght@400;700&display=swap" rel="stylesheet">
<style>
  :root {
    --page-bg: #2a2a2e;
    --brand-blue: #1a93d0;
    --map-blue: #5aa8dc;
    --card-dark: #3e3e46;
    --text-white: #ffffff;
    --accent-blue: #1c8fd0;
  }
  * { margin: 0; padding: 0; box-sizing: border-box; }
  html, body {
    width: 1200px; height: 1189px; overflow: hidden;
    background: var(--page-bg);
    font-family: "Arimo", Arial, sans-serif;
  }
  .card {
    position: absolute; left: 120px; width: 960px; height: 520px;
    border-radius: 34px; overflow: hidden;
  }
  .card-front { top: 50px; background: var(--brand-blue); }
  .card-back { top: 619px; background: var(--card-dark); }

  .world-map {
    position: absolute; left: 120px; top: 60px; width: 740px; height: 380px;
    border-radius: 40% 45% 35% 50%;
    background: radial-gradient(ellipse at center, rgba(120,185,230,0.55) 0%, rgba(120,185,230,0.25) 55%, rgba(120,185,230,0) 75%);
  }
  .front-wordmark {
    position: absolute; left: 0; right: 0; top: 218px;
    display: flex; justify-content: center; align-items: center; gap: 22px;
    color: var(--text-white); font-weight: 700; font-size: 88px; letter-spacing: 6px;
  }
  .front-wordmark .mark-dot {
    width: 70px; height: 70px; border-radius: 50%; background: var(--text-white);
  }

  .back-wordmark {
    position: absolute; left: 70px; top: 225px;
    display: flex; align-items: center; gap: 16px;
    color: var(--accent-blue); font-weight: 700; font-size: 56px; letter-spacing: 4px;
  }
  .back-wordmark .mark-dot {
    width: 50px; height: 50px; border-radius: 50%; background: var(--accent-blue);
  }
  .divider {
    position: absolute; left: 495px; top: 130px; width: 2px; height: 180px;
    background: var(--accent-blue);
  }
  .contact-block { position: absolute; left: 535px; top: 135px; color: var(--text-white); }
  .person-name { color: var(--accent-blue); font-weight: 700; font-size: 30px; letter-spacing: 1px; }
  .person-title { font-size: 22px; margin-top: 2px; }
  .contact-list { list-style: none; margin-top: 26px; }
  .contact-list li { display: flex; align-items: center; gap: 12px; font-size: 22px; height: 34px; }
  .contact-list .icon { width: 26px; height: 26px; flex: none; }
  .contact-list .hl { color: var(--accent-blue); }
  .address {
    position: absolute; left: 0; right: 0; bottom: 90px; text-align: center;
    color: var(--text-white); font-size: 28px;
  }
</style>
</head>
<body>
  <section class="card card-front">
    <div class="world-map" role="img" aria-label="Faint world map in lighter blue"></div>
    <div class="front-wordmark"><span class="mark-dot"></span>TALRENO</div>
  </section>

  <section class="card card-back">
    <div class="back-wordmark"><span class="mark-dot"></span>TALRENO</div>
    <div class="divider"></div>
    <div class="contact-block">
      <div class="person-name">MARA ELLIS</div>
      <div class="person-title">President &amp; CEO</div>
      <ul class="contact-list">
        <li>
          <svg class="icon" viewBox="0 0 26 26"><circle cx="13" cy="13" r="12" fill="none" stroke="#1c8fd0" stroke-width="2"/><path d="M8 10c0-2 2-3 5-3s5 1 5 3l-2 1-1-2h-4l-1 2zM9 13h8l1 5H8z" fill="#1c8fd0"/></svg>
          +01 2468 1357
        </li>
        <li>
          <svg class="icon" viewBox="0 0 26 26"><circle cx="13" cy="13" r="12" fill="none" stroke="#1c8fd0" stroke-width="2"/><rect x="7" y="9" width="12" height="8" fill="#1c8fd0"/><path d="M7 9l6 5 6-5" fill="none" stroke="#3e3e46" stroke-width="1.4"/></svg>
          info@talrenomail.com
        </li>
        <li>
          <svg class="icon" viewBox="0 0 26 26"><circle cx="13" cy="13" r="12" fill="none" stroke="#1c8fd0" stroke-width="2"/><circle cx="13" cy="13" r="7" fill="none" stroke="#1c8fd0" stroke-width="1.5"/><path d="M6 13h14M13 6v14M9 8.5h8M9 17.5h8" stroke="#1c8fd0" stroke-width="1.2"/></svg>
          <span>www.<span class="hl">talrenoweb</span>.com</span>
        </li>
      </ul>
    </div>
    <div class="address">PO BOX 456, Oak Street, 3rd Lane, Leeds</div>
  </section>
</body>
</html>
```